Business Card Design Project

Looking for a simple and stylish business card. We are an Advertising Company. The card Must feature the company logo (attached) and also this info.
p: 0461528390
e: sales@jh-promo.com.au
w: www.jh-promo.com.au
We Advertise mainly using TV screens featured in restaurants and cafe. See website for more about the business.
Not really looking for a plain background, but at the same time do not want to much happening in the Background. I am not really to fussy though with the design or the colour scheme, and I am leaving the creativity part up to you creative designers.
Business

```html
<!DOCTYPE html>
<html lang="en">
<head>
<meta charset="utf-8">
<title>JH Promo – Business Card</title>
<link href="https://fonts.googleapis.com/css2?family=Open+Sans:wght@300;400&display=swap" rel="stylesheet">
<style>
  :root {
    --bg: #e9e6e2;
    --card-white: #f4f4f4;
    --magenta: #d4105c;
    --magenta-dark: #a80a48;
    --navy: #3a2f8c;
    --cyan: #4bb8bd;
    --purple: #8c2a8f;
    --text-light: #ffffff;
  }
  * { margin: 0; padding: 0; box-sizing: border-box; }
  html, body {
    width: 1200px; height: 975px; overflow: hidden;
    background: var(--bg);
    font-family: "Open Sans", Arial, sans-serif;
  }
  .card {
    position: absolute; left: 75px; top: 187px;
    width: 1050px; height: 600px;
    background: var(--card-white);
    overflow: hidden;
    box-shadow: 0 18px 40px rgba(0,0,0,.25);
  }
  .header-art {
    position: absolute; left: 0; top: 0; width: 1050px; height: 245px;
    background: linear-gradient(100deg, #cfd6d8 0%, var(--cyan) 35%, var(--purple) 70%, var(--navy) 100%);
  }
  .brand-band {
    position: absolute; left: 0; top: 245px; width: 1050px; height: 125px;
    background: linear-gradient(180deg, #ffffff 0%, #e8e8e8 100%);
  }
  .brand-name {
    position: absolute; right: 60px; top: 22px;
    font-weight: 300; font-size: 78px; letter-spacing: 2px;
    color: var(--navy); line-height: 1;
  }
  .info-panel {
    position: absolute; left: 0; top: 370px; width: 1050px; height: 230px;
    background: radial-gradient(ellipse at 40% 30%, var(--magenta) 0%, var(--magenta-dark) 100%);
    color: var(--text-light);
  }
  .person { position: absolute; left: 90px; top: 90px; }
  .person-name { font-size: 36px; font-weight: 400; line-height: 1.15; }
  .person-role { font-size: 22px; font-weight: 400; }
  .contact-list { position: absolute; left: 700px; top: 28px; list-style: none; }
  .contact-list li { display: flex; align-items: center; font-size: 21px; line-height: 1.55; }
  .contact-list svg { width: 20px; height: 20px; margin-right: 14px; fill: none; stroke: var(--text-light); stroke-width: 2; }
</style>
</head>
<body>
  <div class="card">
    <div class="header-art" role="img" aria-label="Decorative colour artwork area in grey, cyan, purple and navy tones"></div>
    <div class="brand-band">
      <div class="brand-name">JH PROMO</div>
    </div>
    <div class="info-panel">
      <ul class="contact-list">
        <li>
          <svg viewBox="0 0 24 24"><path d="M5 3h4l2 5-3 2a11 11 0 0 0 6 6l2-3 5 2v4a2 2 0 0 1-2 2A17 17 0 0 1 3 5a2 2 0 0 1 2-2z"/></svg>
          0461528390
        </li>
        <li>
          <svg viewBox="0 0 24 24"><rect x="3" y="5" width="18" height="14" rx="1"/><path d="M3 6l9 7 9-7"/></svg>
          sales@jh-promo.com.au
        </li>
        <li>
          <svg viewBox="0 0 24 24"><circle cx="12" cy="12" r="9"/><path d="M3 12h18M12 3c3 3 3 15 0 18M12 3c-3 3-3 15 0 18"/></svg>
          www.jh-promo.com.au
        </li>
      </ul>
      <div class="person">
        <div class="person-name">Mark Dellaway</div>
        <div class="person-role">Managing Director</div>
      </div>
    </div>
  </div>
</body>
</html>
```